Brenvo Motori - Exotic Auto Parts Catalogue 2025

I'd like to make a product catalogue for my business. We sell Italian auto parts. Think Velotti, Tavinero, Orsi Nuvola, and Zancopetri. We also offer rebuilding services for steering racks, AC compressors, brake calipers, power steering pumps, starter motors, alternators, and sticky switch refinishing. The photos I uploaded are of kits that we offer like valve kits, ignition kits, major service kits, cooling hose kits, brake kits etc. We want to inlcude this catalogue in our packages for first time buyers to show them what we hve to offer and have them keep this on their desk. We also carry upgraded Quarrow Engineering part and are the exclusive North American distributor for Tazlo suspension parts, and exlusive North American distributor for Obruna Systems exhausts

Target Market(s)

Velottti and Zancopetri repair shops and owners

Industry/Entity Type

Automotive

Font styles to use
Serif
Sans Serif

Colors
00AB8E
00BBA5
67D7C9
C6EFE9
E9F9F6
EB3D1F
EC4F4E
F09395
F8D3D4
FCEDEE

Requirements
Must have
• Must be reletively simple. A good amount of white space but enough information for a customer to have this one their desk consistently

```html
<!DOCTYPE html>
<html lang="en">
<head>
<meta charset="utf-8">
<title>Brenvo Motori – Exotic Auto Parts Catalogue 2025</title>
<link rel="stylesheet" href="https://fonts.googleapis.com/css2?family=Montserrat:wght@400;500;600;700;800&display=swap">
<style>
:root{
  --stage:#a6a6a6;
  --paper:#ffffff;
  --green:#1f7a3c;
  --red:#d6262b;
  --ink:#2b2b2b;
  --muted:#666;
  --photo-light:#e6e6e6;
}
*{box-sizing:border-box;margin:0;padding:0}
html,body{width:1200px;height:3997px;overflow:hidden}
body{background:var(--stage);font-family:"Montserrat",sans-serif;color:var(--ink);position:relative}
.spread{position:absolute;left:70px;width:1060px;height:680px;display:flex;box-shadow:0 18px 40px rgba(0,0,0,.28)}
.page{position:relative;width:530px;height:680px;background:var(--paper);overflow:hidden}
.page.left{box-shadow:inset -14px 0 18px -14px rgba(0,0,0,.25)}
.page.right{box-shadow:inset 14px 0 18px -14px rgba(0,0,0,.25)}
.bands{position:absolute;top:0;left:0;width:530px;height:40px}
.page-num{position:absolute;bottom:22px;width:16px;height:12px;background:var(--red);color:#fff;font-size:7px;font-weight:700;text-align:center;line-height:12px}
.left .page-num{left:34px}.right .page-num{right:34px}
.photo{background:linear-gradient(135deg,var(--photo-light),#cfcfcf)}

.product{position:absolute;left:34px;right:34px;display:grid;grid-template-columns:210px 1fr;column-gap:18px;row-gap:10px}
.product .photo{height:130px;border-radius:2px}
.label{display:inline-block;color:#fff;font-weight:700;font-size:11px;padding:5px 22px 5px 12px;clip-path:polygon(0 0,100% 0,88% 100%,0 100%)}
.label.green{background:var(--green)}
.label.red{background:var(--red)}
.desc p,.desc li{font-size:8.5px;line-height:1.55;color:var(--ink)}
.desc strong{font-weight:700}
.desc ul{list-style:none;margin-top:2px}
.desc li::before{content:"✓ ";color:var(--red);font-weight:700}
.desc .label{margin-bottom:6px}
.name-tab{background:var(--green);color:#fff;font-size:10px;font-weight:700;text-align:center;padding:9px 14px;align-self:start;clip-path:polygon(0 0,100% 0,94% 100%,0 100%)}
.info .label{width:100%}
.specs{display:grid;grid-template-columns:60px 1fr;gap:3px 10px;margin:6px 0 6px 12px;font-size:8.5px}
.specs b{font-weight:700}
.price-row{display:flex;align-items:center;gap:10px}
.price-row .key{font-size:10px;font-weight:700;background:var(--green);color:#fff;padding:4px 14px}
.price{background:var(--red);color:#fff;font-size:12px;font-weight:800;padding:6px 26px;clip-path:polygon(0 0,100% 0,92% 100%,0 100%)}

.about-hero{position:absolute;top:0;left:0;width:530px;height:220px}
.about-tag{position:absolute;top:28px;left:34px;background:var(--green);color:#fff;font-weight:800;font-size:11px;padding:5px 22px}
.about-head{position:absolute;top:66px;left:34px;width:250px;color:#fff;font-weight:800;font-size:15px;line-height:1.25;text-transform:uppercase}
.about-photo{position:absolute;top:50px;left:300px;width:190px;height:140px}
.about-title{position:absolute;top:250px;left:34px;font-size:17px;font-weight:800}
.about-body{position:absolute;top:285px;left:34px;right:40px;font-size:8.5px;line-height:1.7;color:var(--muted)}
.about-body p{margin-bottom:10px}

.back-photo{position:absolute;top:0;left:0;width:530px;height:340px;background:linear-gradient(160deg,#bdbdbd,#6f6f6f)}
.back-tint{position:absolute;top:0;left:0;width:530px;height:340px}
.back-title{position:absolute;top:228px;left:150px;color:#fff;font-weight:800;font-size:20px}
.contacts{position:absolute;top:370px;left:34px;width:320px;list-style:none}
.contacts li{display:flex;align-items:center;margin-bottom:10px;font-size:9.5px;font-weight:600;color:#fff}
.contacts .ico{flex:none;width:26px;height:22px;background:var(--green);display:flex;align-items:center;justify-content:center}
.contacts .txt{background:var(--red);padding:5px 18px 5px 10px;clip-path:polygon(0 0,100% 0,94% 100%,0 100%)}
.contacts li.wide .txt{font-size:8.5px}
.follow{position:absolute;top:420px;right:40px;font-size:9px;font-weight:700}
.follow span{display:inline-block;width:12px;height:12px;background:var(--green);margin:5px 4px 0 0}
.front-art{position:absolute;inset:0}
.logo{position:absolute;top:50px;left:215px;display:flex;align-items:center;gap:8px;background:#fff;padding:10px 16px;border:2px solid var(--green)}
.logo i{width:14px;height:14px;border-radius:50%;background:var(--red)}
.logo span{font-weight:800;font-size:17px;color:var(--red)}
.headline{position:absolute;top:140px;left:70px;right:30px;color:#fff;font-weight:800;font-size:19px;line-height:1.3;text-align:center;text-transform:uppercase}
.car-photo{position:absolute;top:270px;left:115px;width:300px;height:190px;border-radius:6px;background:linear-gradient(160deg,#dfe3e6,#8e979c)}

.exhaust-lists{position:absolute;top:170px;left:34px;right:34px;display:grid;grid-template-columns:1fr 1fr;gap:20px}
.exhaust-lists h4{font-size:8.5px;font-weight:800;margin:8px 0 3px}
.intro-text{position:absolute;top:70px;left:34px;right:34px;font-size:9px;line-height:1.7;color:var(--muted)}
.intro-text .fits{text-align:right;font-size:8.5px;color:var(--ink);margin-bottom:8px}
</style>
</head>
<body>

<svg width="0" height="0" style="position:absolute" aria-hidden="true">
  <defs>
    <g id="bands-left"><polygon points="0,0 330,0 300,18 0,18" fill="#d6262b"/><polygon points="330,0 530,0 530,18 300,18" fill="#1f7a3c"/></g>
    <g id="bands-right"><polygon points="0,0 200,0 230,18 0,18" fill="#1f7a3c"/><polygon points="200,0 530,0 530,18 230,18" fill="#d6262b"/></g>
  </defs>
</svg>

<!-- Spread 1: covers -->
<section class="spread" style="top:60px">
  <div class="page left">
    <div class="back-photo" role="img" aria-label="Photograph of red sports cars parked at a showroom"></div>
    <svg class="back-tint" viewBox="0 0 530 340" aria-hidden="true"><path d="M0,120 Q260,190 530,250 L530,340 L0,340 Z" fill="#1f7a3c" opacity=".88"/></svg>
    <p class="back-title">We're Ready To Help You!</p>
    <ul class="contacts">
      <li><span class="ico"><svg width="12" height="12" viewBox="0 0 24 24"><path fill="#fff" d="M6.6 10.8a15 15 0 0 0 6.6 6.6l2.2-2.2a1 1 0 0 1 1-.25 11.4 11.4 0 0 0 3.6.6 1 1 0 0 1 1 1V20a1 1 0 0 1-1 1A17 17 0 0 1 3 4a1 1 0 0 1 1-1h3.5a1 1 0 0 1 1 1c0 1.25.2 2.45.6 3.6a1 1 0 0 1-.25 1z"/></svg></span><span class="txt">555-014-2200 | 800-555-0147</span></li>
      <li><span class="ico"><svg width="12" height="10" viewBox="0 0 24 18"><rect x="1" y="1" width="22" height="16" fill="none" stroke="#fff" stroke-width="2"/><path d="M1 1l11 9 11-9" fill="none" stroke="#fff" stroke-width="2"/></svg></span><span class="txt">hello@brenvomotori.example</span></li>
      <li><span class="ico"><svg width="12" height="12" viewBox="0 0 24 24"><circle cx="12" cy="12" r="10" fill="none" stroke="#fff" stroke-width="2"/><path d="M12 6v6l4 2" stroke="#fff" stroke-width="2" fill="none"/></svg></span><span class="txt">Monday – Friday 8:00 to 6:00 PM EST</span></li>
      <li class="wide"><span class="ico"><svg width="10" height="13" viewBox="0 0 20 26"><path fill="#fff" d="M10 0a9 9 0 0 0-9 9c0 7 9 17 9 17s9-10 9-17a9 9 0 0 0-9-9zm0 12a3 3 0 1 1 0-6 3 3 0 0 1 0 6z"/></svg></span><span class="txt">48 Corsa Lane, Millbrook, NJ 07001 Corner of Route 9 and Corsa Lane</span></li>
    </ul>
    <div class="follow">Follow Us:<br><span></span><span></span></div>
    <svg style="position:absolute;bottom:0;left:0" width="530" height="80" viewBox="0 0 530 80" aria-hidden="true"><polygon points="0,62 530,20 530,32 0,74" fill="#d6262b"/></svg>
  </div>
  <div class="page right">
    <svg class="front-art" viewBox="0 0 530 680" aria-hidden="true">
      <path d="M0,0 L530,0 L530,80 Q300,40 60,110 Z" fill="#fff"/>
      <polygon points="40,130 530,90 530,250 0,300" fill="#1f7a3c"/>
      <polygon points="0,470 530,380 530,680 250,680" fill="#d6262b"/>
      <polygon points="0,470 250,680 0,680" fill="#fff"/>
    </svg>
    <div class="logo"><i></i><span>Brenvo Motori</span></div>
    <p class="headline">Culture is the foundation<br>upon which all success is built</p>
    <div class="car-photo" role="img" aria-label="Photograph of a white Orsi Nuvola SUV"></div>
  </div>
</section>

<!-- Spread 2: about + engine kits -->
<section class="spread" style="top:850px">
  <div class="page left">
    <svg class="about-hero" viewBox="0 0 530 220" aria-hidden="true"><polygon points="0,0 530,0 530,110 0,220" fill="#d6262b"/><polygon points="0,0 530,0 530,8 0,8" fill="#1f7a3c"/></svg>
    <span class="about-tag">ABOUT US</span>
    <p class="about-head">OE parts or reputable European and U.S. manufactures – only.</p>
    <div class="about-photo photo" role="img" aria-label="Photograph of the team in the parts showroom"></div>
    <h2 class="about-title">Welcome to Brenvo Motori Auto Parts!</h2>
    <div class="about-body">
      <p>Our story began in 1986 when Dario Benvetti saw a gap in the local supply of Italian parts. What started as a small counter grew into a trusted source for shops and owners across the country, built on honest advice and parts that fit the first time.</p>
      <p>We take pride in our family-run team, many of whom have worked with us for decades. We listen, we check every part number, and we ship quickly so your car spends less time on the lift.</p>
      <p>We endeavor to source our parts from only the most reliable OE and OEM manufacturers, and we rebuild racks, pumps and calipers in house. Thank you for choosing us – we look forward to serving you for years to come.</p>
    </div>
    <span class="page-num">1</span>
  </div>
  <div class="page right">
    <svg class="bands" viewBox="0 0 530 40"><use href="#bands-right"/></svg>
    <div class="product" style="top:55px">
      <div class="photo" role="img" aria-label="Photograph of a full engine gasket set laid out"></div>
      <div class="desc"><span class="label green">Description</span>
        <p>Velotti Full Engine Gasket Set<br>– With Original Fitted Head Gaskets</p>
        <p><strong>Fits The Following:</strong> V28 Orbiale 3.2</p>
        <p><strong>Part Number:</strong> BM-40218</p></div>
      <div class="name-tab">Velotti V28 &amp; Orbiale 3.2 Engine Gasket Set</div>
      <div class="info"><span class="label red">Additional Information</span>
        <div class="specs"><b>Weight</b><span>7 lbs</span><b>Dimensions</b><span>24 × 17 × 7 in</span></div>
        <div class="price-row"><span class="key">Price</span><span class="price">$1,500.00</span></div></div>
    </div>
    <div class="product" style="top:345px">
      <div class="photo" role="img" aria-label="Photograph of intake and exhaust valves with guides"></div>
      <div class="desc"><span class="label green">Description</span>
        <p>Velotti Engine Valve Kit</p>
        <p><strong>Fits The Following:</strong> V35</p>
        <p><strong>Part Number:</strong> BM-51730K</p>
        <p><strong>Includes:</strong></p>
        <ul><li>24 Intake Valves &amp; Guides</li><li>16 Exhaust Valves &amp; Guides</li><li>40 Valve Stem Seals</li></ul></div>
      <div class="name-tab">Velotti V35 Engine Valve Kit</div>
      <div class="info"><span class="label red">Additional Information</span>
        <div class="specs"><b>Weight</b><span>6 lbs</span><b>Dimensions</b><span>7 × 7 × 7 in</span></div>
        <div class="price-row"><span class="key">Price</span><span class="price">$3,500.00</span></div></div>
    </div>
    <span class="page-num">2</span>
  </div>
</section>

<!-- Spread 3: suspension + exhaust -->
<section class="spread" style="top:1640px">
  <div class="page left">
    <svg class="bands" viewBox="0 0 530 40"><use href="#bands-left"/></svg>
    <div class="product" style="top:55px">
      <div class="photo" role="img" aria-label="Photograph of front suspension bushings and links"></div>
      <div class="desc"><span class="label green">Description</span>
        <p>Velotti V36/V43 Complete Front Suspension Kit</p>
        <p><strong>Fits The Following:</strong> V36, V43</p>
        <p><strong>Part Number:</strong> BM-SK3604</p>
        <p><strong>Includes:</strong></p>
        <ul><li>4 Lower Control Arm Bushings</li><li>4 Upper Arm Bushings</li><li>2 Ball Joints With Boots</li><li>2 Sway Bar Links</li></ul></div>
      <div class="name-tab">Velotti V36 &amp; V43 Suspension Kit</div>
      <div class="info"><span class="label red">Additional Information</span>
        <div class="specs"><b>Weight</b><span>5 lbs</span><b>Dimensions</b><span>7 × 7 × 7 in</span></div>
        <div class="price-row"><span class="key">Price</span><span class="price">$2,050.00</span></div></div>
    </div>
    <div class="product" style="top:380px">
      <div class="photo" role="img" aria-label="Photograph of a stainless exhaust muffler assembly"></div>
      <div class="desc"><span class="label green">Description</span>
        <p>G12 Exhaust Muffler Assembly by Obruna Systems</p>
        <p><strong>Fits the following:</strong> G12 Corsa</p>
        <p><strong>Part Number:</strong> OB-77120</p></div>
    </div>
    <span class="page-num">3</span>
  </div>
  <div class="page right">
    <svg class="bands" viewBox="0 0 530 40"><use href="#bands-right"/></svg>
    <div class="product" style="top:60px">
      <div class="name-tab">Velotti V58 Exhaust</div>
      <div class="info"><span class="label red">Additional Information</span>
        <div class="specs"><b>Weight</b><span>38 lbs</span><b>Dimensions</b><span>43 × 21 × 13 in</span></div>
        <div class="price-row"><span class="key">Price</span><span class="price">$5,308.40</span></div></div>
    </div>
    <div class="exhaust-lists desc">
      <div>
        <h4>ADVANCED CONSTRUCTION</h4>
        <ul><li>CAD Designed &amp; CNC Executed</li><li>Aviation Grade T-304 Stainless</li><li>Double Walled Casing</li><li>Thermal Barrier Wrap</li><li>Laser Cut Mounting Flanges</li></ul>
        <h4>SUPERIOR SOUND</h4>
        <ul><li>Deeper Low Level Tone</li><li>Aggressive Mid-Range Note</li><li>Tuned Lower Noise Under Load</li><li>Distinctive Tone</li></ul>
        <h4>LEADING GAINS</h4>
        <ul><li>Noticeable Bhp Gain Typically</li><li>Lower Back Pressure</li><li>Sharper Throttle Response</li><li>Reduced Weight Over OE</li></ul>
      </div>
      <div>
        <ul><li>Tig Welded Assembly</li><li>Heat Resistant Shield Inserts</li><li>Valve Control Retained</li><li>Dual Mode Sound Settings</li><li>Direct Bolt-On Fitment</li></ul>
        <ul style="margin-top:12px"><li>Sharper, Crisper Sound Across The Rev Range</li><li>Refined Cruise With No Drone</li><li>Protective Coating Inside And Out</li></ul>
        <ul style="margin-top:12px"><li>Controlled Temperatures For Added Performance</li><li>Engineered In Keeping With The Engine Mapping</li><li>Vastly Freer Flowing Than OE</li></ul>
      </div>
    </div>
    <span class="page-num">4</span>
  </div>
</section>

<!-- Spread 4: service kit + shocks + ignition -->
<section class="spread" style="top:2430px">
  <div class="page left">
    <svg class="bands" viewBox="0 0 530 40"><use href="#bands-left"/></svg>
    <div class="product" style="top:55px">
      <div class="photo" role="img" aria-label="Photograph of a major service kit with belts, filters and gaskets"></div>
      <div class="desc"><span class="label green">Description</span>
        <p>Major Service Kit for Velotti V52M</p>
        <p><strong>Part Number:</strong> BM-SK5209</p>
        <p><strong>Includes:</strong></p>
        <ul><li>2 Timing Belts</li><li>2 Tensioner Bearings</li><li>1 Oil Filter</li><li>1 Fuel Filter</li><li>12 Spark Plugs</li><li>Cam Cover Gaskets</li></ul></div>
      <div class="name-tab">Velotti V52M Major Service Kit</div>
      <div class="info"><span class="label red">Additional Information</span>
        <div class="specs"><b>Weight</b><span>8 lbs</span><b>Dimensions</b><span>30 × 14 × 6 in</span></div>
        <div class="price-row"><span class="key">Price</span><span class="price">$1,395.00</span></div></div>
    </div>
    <div class="product" style="top:400px">
      <div class="photo" role="img" aria-label="Photograph of a rear shock absorber"></div>
      <div class="desc"><span class="label green">Description</span>
        <p>Velotti Rear Shock Absorber</p>
        <p><strong>Fits the following:</strong> G12 Corsa</p>
        <p><strong>Part Number:</strong> BM-60915</p></div>
    </div>
    <span class="page-num">5</span>
  </div>
  <div class="page right">
    <svg class="bands" viewBox="0 0 530 40"><use href="#bands-right"/></svg>
    <div class="product" style="top:60px">
      <div class="name-tab">Velotti G12 Shock Absorber</div>
      <div class="info"><span class="label red">Additional Information</span>
        <div class="specs"><b>Weight</b><span>6 lbs</span><b>Dimensions</b><span>26 × 6 × 6 in</span></div>
        <div class="price-row"><span class="key">Price</span><span class="price">$1,075.85</span></div></div>
    </div>
    <div class="product" style="top:220px">
      <div class="photo" role="img" aria-label="Photograph of a red ignition lead kit with coils"></div>
      <div class="desc"><span class="label green">Description</span>
        <p>Velotti Rossaline Ignition Kit</p>
        <p><strong>Fits The Following:</strong> Rossaline</p>
        <p><strong>Part Number:</strong> BM-IG2041</p></div>
      <div class="name-tab">Velotti Rossaline Ignition Kit</div>
      <div class="info"><span class="label red">Additional Information</span>
        <div class="specs"><b>Weight</b><span>3 lbs</span><b>Dimensions</b><span>12 × 12 × 6 in</span></div>
        <div class="price-row"><span class="key">Price</span><span class="price">$1,765.00</span></div></div>
    </div>
    <span class="page-num">6</span>
  </div>
</section>

<!-- Spread 5: brake kits -->
<section class="spread" style="top:3220px">
  <div class="page left">
    <svg class="bands" viewBox="0 0 530 40"><use href="#bands-left"/></svg>
    <div class="product" style="top:55px">
      <div class="photo" role="img" aria-label="Photograph of front and rear brake rotors with pads"></div>
      <div class="desc"><span class="label green">Description</span>
        <p>Zancopetri Galvero Front &amp; Rear Brake Pad &amp; Rotor Kit for cars without ceramic rotors</p>
        <p><strong>Fits The Following:</strong> Galvero S5 Coupe and Spyder</p>
        <p><strong>Part Number:</strong> BM-ZBR88</p>
        <p><strong>Includes:</strong></p>
        <ul><li>(2) Front Rotors</li><li>(2) Rear Rotors</li><li>Front &amp; Rear Pad Sets</li></ul></div>
      <div class="name-tab">Zancopetri Galvero Front Brake Kit</div>
      <div class="info"><span class="label red">Additional Information</span>
        <div class="specs"><b>Weight</b><span>45 lbs</span><b>Dimensions</b><span>18 × 18 × 16 in</span></div>
        <div class="price-row"><span class="key">Price</span><span class="price">$2,260.00</span></div></div>
    </div>
    <div class="product" style="top:400px">
      <div class="photo" role="img" aria-label="Photograph of brake rotors and a pad set box"></div>
      <div class="desc"><span class="label green">Description</span>
        <p>Tavinero Levanza Rear Brake Rotors &amp; Pads Kit – Premium quality rotors from Calvatti OE</p>
        <p><strong>Includes:</strong></p>
        <ul><li>TV-311402 (left rotor)</li><li>TV-311403 (right rotor)</li><li>TV-310618 (rear pads)</li></ul></div>
    </div>
    <span class="page-num">7</span>
  </div>
  <div class="page right">
    <svg class="bands" viewBox="0 0 530 40"><use href="#bands-right"/></svg>
    <div class="intro-text">
      <p class="fits"><strong>Fits The Following:</strong> Levanza (w/ smooth rotors)<br><strong>Part Number:</strong> TV-311402K</p>
      <p>Enhance the braking performance of your Tavinero Levanza with our comprehensive Rear Brake Kit. This kit includes high-quality brake pads and rotors designed for exceptional stopping power and durability. Precision-engineered for a perfect fit, it ensures consistent braking performance in all driving conditions. Upgrade your Tavinero Levanza today with this essential Brake Kit for superior quality and peace of mind on the road.</p>
    </div>
    <div class="product" style="top:300px">
      <div class="name-tab">Tavinero Levanza Rear Brake Kit</div>
      <div class="info"><span class="label red">Additional Information</span>
        <div class="specs"><b>Weight</b><span>75 lbs</span><b>Dimensions</b><span>14 × 14 × 6 in</span></div>
        <div class="price-row"><span class="key">Price</span><span class="price">$380.00</span></div></div>
    </div>
    <span class="page-num">8</span>
  </div>
</section>

</body>
</html>
```